serious, thorough, light and simple - that's my advice and mediations

My business card should combine my logo (uploaded file) and my homepage (https://feltra-mediation.plavosite.com).

Contact Information for Business Card

Name: Sabine Feltra di Olvesi
Phone: 079 417 68 92
mail: sfeltra@plovix.ch
web: www.feltra-di-olvesi.ch

```html
<!DOCTYPE html>
<html lang="de">
<head>
<meta charset="utf-8">
<title>Visitenkarte – Sabine Feltra di Olvesi</title>
<link rel="stylesheet" href="https://fonts.googleapis.com/css2?family=Montserrat:wght@400;500&display=swap">
<style>
  :root {
    --page-bg: #e4e4e4;
    --brand-green: #02683a;
    --brand-gold: #a8843f;
    --card-white: #ffffff;
    --text-dark: #333333;
    --icon-blue: #2e3e8c;
    --divider: #9a9a9a;
  }
  * { margin: 0; padding: 0; box-sizing: border-box; }
  html, body {
    width: 1200px;
    height: 896px;
    overflow: hidden;
    background: var(--page-bg);
    font-family: "Montserrat", sans-serif;
  }
  .canvas {
    position: relative;
    width: 1200px;
    height: 896px;
  }
  .card {
    position: absolute;
    left: 302px;
    width: 619px;
    height: 354px;
    box-shadow: 0 3px 8px rgba(0, 0, 0, 0.25);
  }
  .card--front { top: 95px; background: var(--brand-green); }
  .card--back  { top: 469px; background: var(--card-white); }

  .brand {
    position: absolute;
    display: flex;
    align-items: center;
    gap: 12px;
    font-weight: 500;
    color: var(--brand-gold);
    white-space: nowrap;
  }
  .brand__dot {
    border-radius: 50%;
    flex: none;
  }
  .card--front .brand {
    left: 50%;
    top: 50%;
    transform: translate(-50%, -50%);
    font-size: 40px;
  }
  .card--front .brand__dot { width: 30px; height: 30px; background: var(--card-white); }
  .card--back .brand {
    left: 74px;
    top: 178px;
    transform: translateY(-50%);
    font-size: 24px;
  }
  .card--back .brand__dot { width: 20px; height: 20px; background: var(--brand-green); }

  .divider {
    position: absolute;
    left: 316px;
    top: 95px;
    width: 1px;
    height: 164px;
    background: var(--divider);
  }
  .contact {
    position: absolute;
    left: 337px;
    top: 94px;
    color: var(--text-dark);
  }
  .contact__name {
    font-size: 20px;
    font-weight: 500;
    color: var(--brand-green);
    line-height: 24px;
  }
  .contact__role {
    font-size: 14px;
    line-height: 18px;
    margin-top: 1px;
  }
  .contact__label {
    font-size: 17px;
    color: var(--brand-gold);
    margin-top: 12px;
    line-height: 20px;
  }
  .contact__homepage {
    font-size: 14.5px;
    line-height: 18px;
    margin-top: 2px;
  }
  .contact__list {
    list-style: none;
    margin-top: 14px;
    font-size: 14.5px;
  }
  .contact__item {
    display: flex;
    align-items: center;
    gap: 7px;
    line-height: 18.5px;
  }
  .contact__icon { width: 11px; height: 11px; fill: var(--icon-blue); flex: none; }
</style>
</head>
<body>
<main class="canvas">
  <section class="card card--front" aria-label="Vorderseite">
    <div class="brand"><span class="brand__dot"></span><span class="brand__name">Wege im Dialog</span></div>
  </section>

  <section class="card card--back" aria-label="Rückseite">
    <div class="brand"><span class="brand__dot"></span><span class="brand__name">Wege im Dialog</span></div>
    <div class="divider"></div>
    <div class="contact">
      <p class="contact__name">Sabine Feltra di Olvesi</p>
      <p class="contact__role">CEO</p>
      <p class="contact__label">Homepage</p>
      <p class="contact__homepage">feltra-mediation.plavosite.com</p>
      <ul class="contact__list">
        <li class="contact__item">
          <svg class="contact__icon" viewBox="0 0 24 24" aria-hidden="true"><path d="M6.6 10.8c1.4 2.8 3.8 5.1 6.6 6.6l2.2-2.2c.3-.3.7-.4 1-.2 1.1.4 2.3.6 3.6.6.6 0 1 .4 1 1V20c0 .6-.4 1-1 1C10.6 21 3 13.4 3 4c0-.6.4-1 1-1h3.5c.6 0 1 .4 1 1 0 1.3.2 2.5.6 3.6.1.3 0 .7-.2 1L6.6 10.8z"/></svg>
          <span>079 417 68 92</span>
        </li>
        <li class="contact__item">
          <svg class="contact__icon" viewBox="0 0 24 24" aria-hidden="true"><path d="M2 5h20v14H2z M2 5l10 8 10-8" fill="var(--icon-blue)" stroke="#fff" stroke-width="1.5"/></svg>
          <span>sfeltra@plovix.ch</span>
        </li>
        <li class="contact__item">
          <svg class="contact__icon" viewBox="0 0 24 24" aria-hidden="true"><circle cx="12" cy="12" r="10"/><path d="M2 12h20M12 2v20M5 6.5h14M5 17.5h14" stroke="#fff" stroke-width="1.3" fill="none"/></svg>
          <span>www.feltra-di-olvesi.ch</span>
        </li>
      </ul>
    </div>
  </section>
</main>
</body>
</html>
```